real esate business card with company logo and name

we need a business card design for a real esate company

The company name is Walsh & Brody Pty Ltd, and we have our logo designed and will upload. We want classic or moden feel. Black or white background. looks more textured. Should include folowinginformations
Paul Walsh and Lucy Brody
Sales Agents & Onsite Manager
p: 07 5948 2063
F: 07 5948 2174
M:0461 857 239
3/42 Marlin Crescent, HARLOW VALE QLD 4095

We want this business card looks professonal. Thank you in advance.

Industry/Entity Type

Real Estate Agent

Contact Information for Business Card

Paul Walsh and Lucy Brody
Onsite Manager & Sales Agents
p: 07 5948 2063
M:0461 857 239

Font styles to use
Serif

Colors
000000
fbfbfb
333333
959595

Requirements
Must have
• company logo and name, black or white back ground

```html
<!DOCTYPE html>
<html lang="en">
<head>
<meta charset="utf-8">
<title>Walsh &amp; Brody Pty Ltd — Business Card</title>
<link rel="stylesheet" href="https://fonts.googleapis.com/css2?family=Roboto+Condensed:wght@400&family=Source+Sans+3:wght@400&display=swap">
<style>
  :root {
    --backdrop: #a8a6a7;
    --card: #141518;
    --mark: #5f6164;
    --brand-text: #8b8d90;
    --name-text: #d2d3d5;
    --detail-text: #b9babd;
  }
  * { margin: 0; padding: 0; box-sizing: border-box; }
  html, body {
    width: 1200px;
    height: 1200px;
    overflow: hidden;
    background: var(--backdrop);
  }
  .canvas { position: relative; width: 1200px; height: 1200px; }

  .card {
    position: absolute;
    width: 712px;
    height: 418px;
    background: var(--card);
    border-radius: 28px;
  }
  .card--front { left: 238px; top: 118px; }
  .card--back  { left: 231px; top: 644px; }

  .brand {
    position: absolute;
    display: flex;
    flex-direction: column;
    align-items: center;
  }
  .brand__square {
    width: 120px;
    height: 120px;
    background: var(--mark);
  }
  .brand__name {
    margin-top: 34px;
    font-family: "Roboto Condensed", sans-serif;
    font-weight: 400;
    font-size: 24px;
    letter-spacing: 0.3px;
    color: var(--brand-text);
    white-space: nowrap;
  }
  .card--front .brand { left: 0; right: 0; top: 140px; }
  .card--back .brand { left: 40px; width: 300px; top: 136px; }

  .contact { position: absolute; left: 373px; top: 88px; }
  .contact__names {
    font-family: "Roboto Condensed", sans-serif;
    font-weight: 400;
    font-size: 26px;
    color: var(--name-text);
    white-space: nowrap;
  }
  .contact__role {
    margin-top: 8px;
    font-family: "Roboto Condensed", sans-serif;
    font-weight: 400;
    font-size: 15.5px;
    color: var(--detail-text);
  }
  .contact__lines { margin-top: 42px; list-style: none; }
  .contact__line {
    display: flex;
    align-items: center;
    height: 26.5px;
    font-family: "Source Sans 3", sans-serif;
    font-size: 18px;
    color: var(--detail-text);
  }
  .contact__icon { width: 18px; height: 18px; margin: 0 17px 0 1px; fill: var(--detail-text); }
  .contact__address {
    margin-top: 4px;
    font-family: "Source Sans 3", sans-serif;
    font-size: 18px;
    line-height: 28px;
    color: var(--detail-text);
    font-style: normal;
  }
</style>
</head>
<body>
<main class="canvas">

  <section class="card card--front" aria-label="Card front">
    <div class="brand">
      <div class="brand__square"></div>
      <p class="brand__name">WALSH &amp; BRODY PTY LTD.</p>
    </div>
  </section>

  <section class="card card--back" aria-label="Card back">
    <div class="brand">
      <div class="brand__square"></div>
      <p class="brand__name">WALSH &amp; BRODY PTY LTD.</p>
    </div>

    <div class="contact">
      <h1 class="contact__names">Paul Walsh &amp; Lucy Brody</h1>
      <p class="contact__role">Sales Agents &amp; Onsite Manager</p>
      <ul class="contact__lines">
        <li class="contact__line">
          <svg class="contact__icon" viewBox="0 0 18 18" aria-label="Mobile">
            <path d="M5 1h8a1 1 0 0 1 1 1v14a1 1 0 0 1-1 1H5a1 1 0 0 1-1-1V2a1 1 0 0 1 1-1zm1 2v10h6V3zm3 11a1 1 0 1 0 0 2 1 1 0 0 0 0-2z"/>
          </svg>
          0461 857 239
        </li>
        <li class="contact__line">
          <svg class="contact__icon" viewBox="0 0 18 18" aria-label="Phone">
            <path d="M1 6c0-2 4-3 8-3s8 1 8 3v1.5h-4V6H5v1.5H1zM5 8h8l3 4v4H2v-4zm4 2.5a2 2 0 1 0 0 4 2 2 0 0 0 0-4z"/>
          </svg>
          07 5948 2063
        </li>
        <li class="contact__line">
          <svg class="contact__icon" viewBox="0 0 18 18" aria-label="Fax">
            <path d="M5 1h8v4H5zM2 6h14a1 1 0 0 1 1 1v6h-3v4H4v-4H1V7a1 1 0 0 1 1-1zm4 6v3.5h6V12z"/>
          </svg>
          07 5948 2174
        </li>
      </ul>
      <address class="contact__address">3/42 Marlin Crescent,<br>HARLOW VALE QLD 4095</address>
    </div>
  </section>

</main>
</body>
</html>
```